Harbor Oncology Partners Patient Referral Card

We need a 3.75" wide by 8.25" long patient referral card that a physician will fill out to refer their patient to Harbor Oncology Partners. The front of the card will have our logo on top, followed by contact information, a map that shows the office location and then there will be descriptive text at the bottom. On the back side, there will be a headshot photo with a brief bio of Dr. Marcus Whitfield. The address for the office is: 4175 N. Larchmont, Puyallup, WA 98461. The office phone number is 253.400.7218 and the website address is: harboroncologyhub.com

Target Market(s)

Physicians and medical staff

Font styles to use
Serif

Colors
34a7d8
33b8a4
9bcb3c

Requirements
Must have
• A map of the office location and two text boxes for descriptive language about services, and a photo and bio of Dr. Marcus Whitfield
Nice to have
• Clean and distinct design that is eye catching
Should not have
• Flowery or bold colors that distract from the content and purpose of the card

```html
<!DOCTYPE html>
<html lang="en">
<head>
<meta charset="utf-8">
<title>Harbor Oncology Partners – Referral Card</title>
<link rel="stylesheet" href="https://fonts.googleapis.com/css2?family=Montserrat:wght@400;500&family=Roboto:wght@300;500;700&family=Roboto+Condensed:ital,wght@1,500&family=Oswald:wght@500&display=swap">
<style>
  :root {
    --frame: #1c5b6b;
    --panel-grey: #e6e6e7;
    --white: #ffffff;
    --teal: #2bb3b6;
    --green-teal: #33b8a4;
    --sky: #34a7d8;
    --ink: #4a4a4a;
    --ink-dark: #1d1d1d;
    --map-grey: #f1f1f1;
    --map-border: #bdbdbd;
    --photo-teal: #27b4bf;
  }
  * { margin: 0; padding: 0; box-sizing: border-box; }
  html, body { width: 1200px; height: 1119px; overflow: hidden; background: var(--frame); }
  .canvas { position: relative; width: 1200px; height: 1119px; background: var(--frame); }

  .front { position: absolute; left: 26px; top: 32px; width: 1149px; height: 522px; background: var(--panel-grey); }
  .brand-mark { position: absolute; left: 95px; top: 92px; width: 180px; height: 180px; border-radius: 50%; background: var(--green-teal); opacity: .85; }
  .brand-name { position: absolute; left: 294px; top: 62px; font-family: "Montserrat", sans-serif; font-weight: 400; font-size: 60px; line-height: 76px; letter-spacing: 2px; color: var(--teal); }
  .tagline { position: absolute; left: 66px; top: 322px; font-family: "Montserrat", sans-serif; font-weight: 500; font-size: 21px; letter-spacing: 13.5px; color: var(--ink); white-space: nowrap; }

  .contact-box { position: absolute; left: 98px; top: 362px; width: 386px; height: 160px; background: var(--white); border-radius: 30px 30px 0 0; }
  .contact-row { position: absolute; left: 36px; display: flex; align-items: center; gap: 10px; font-family: "Roboto", sans-serif; font-weight: 500; color: var(--ink); white-space: nowrap; }
  .contact-row svg { width: 32px; height: 32px; flex: none; }
  .contact-row.phone { top: 16px; font-size: 29px; font-weight: 700; }
  .contact-row.web { top: 58px; font-size: 20px; }
  .contact-row.mail { top: 102px; font-size: 20px; }

  .map { position: absolute; left: 652px; top: 40px; width: 441px; height: 365px; border: 4px solid var(--map-border); background: linear-gradient(160deg, #f5f5f5, #e9e9e9); }
  .address { position: absolute; left: 636px; top: 432px; display: flex; align-items: center; gap: 12px; font-family: "Roboto", sans-serif; font-weight: 500; font-size: 22px; color: var(--ink); white-space: nowrap; }
  .address svg { width: 52px; height: 52px; }

  .back { position: absolute; left: 26px; top: 573px; width: 1149px; height: 523px; background: var(--white); }
  .headshot { position: absolute; left: 88px; top: 65px; width: 264px; height: 356px; border: 4px solid #7d7d7d; background: linear-gradient(180deg, var(--photo-teal), #22a9b2 60%, #2f3d48); }
  .caption { position: absolute; left: 0; top: 438px; width: 440px; text-align: center; font-family: "Roboto", sans-serif; font-weight: 300; font-size: 19px; line-height: 24px; color: var(--ink); }

  .headline-band { position: absolute; left: 380px; top: 0; width: 769px; height: 79px; background: var(--green-teal); border-radius: 0 0 0 40px; display: flex; align-items: center; justify-content: center; }
  .headline { font-family: "Oswald", sans-serif; font-weight: 500; font-size: 29px; color: var(--ink-dark); }

  .about-box { position: absolute; left: 380px; top: 99px; width: 769px; height: 424px; background: var(--sky); border-radius: 60px 60px 0 0; padding: 12px 44px 0; text-align: center; font-family: "Roboto Condensed", sans-serif; font-style: italic; font-weight: 500; font-size: 18px; line-height: 33px; color: var(--white); }
  .about-box p + p { margin-top: 17px; }
  .about-box p.spaced { margin-top: 33px; }
</style>
</head>
<body>
<div class="canvas">

  <section class="front">
    <div class="brand-mark"></div>
    <div class="brand-name">Harbor<br>Oncology<br>Partners</div>
    <div class="tagline">RADIATION ONCOLOGY</div>

    <div class="contact-box">
      <div class="contact-row phone">
        <svg viewBox="0 0 32 32"><circle cx="16" cy="16" r="16" fill="#2bb3b6"/><path d="M11 8.5c.8-.5 1.6-.3 2 .4l1.6 2.8c.4.7.2 1.4-.4 1.8l-1.1.8c.6 1.8 2 3.6 3.8 4.7l1-1c.5-.6 1.3-.6 1.9-.2l2.7 1.8c.7.5.8 1.3.3 2l-1.2 1.6c-.8 1-2.3 1.3-3.8.6C12.8 21.7 9.5 17.6 8.6 13c-.3-1.6.2-3.3 1.3-4.1z" fill="#fff"/></svg>
        253-400-7218
      </div>
      <div class="contact-row web">
        <svg viewBox="0 0 32 32"><circle cx="16" cy="16" r="16" fill="#2bb3b6"/><g fill="none" stroke="#fff" stroke-width="1.5"><circle cx="16" cy="16" r="9"/><ellipse cx="16" cy="16" rx="4" ry="9"/><path d="M7 16h18M8.5 11.5h15M8.5 20.5h15"/></g></svg>
        www.harboroncologyhub.com
      </div>
      <div class="contact-row mail">
        <svg viewBox="0 0 32 32"><circle cx="16" cy="16" r="16" fill="#2bb3b6"/><rect x="8" y="10.5" width="16" height="11" fill="none" stroke="#fff" stroke-width="1.6"/><path d="M8 10.5l8 6.5 8-6.5" fill="none" stroke="#fff" stroke-width="1.6"/></svg>
        care@harboroncologyhub.com
      </div>
    </div>

    <div class="map" role="img" aria-label="Street map of Puyallup showing the office location"></div>

    <div class="address">
      <svg viewBox="0 0 52 52"><circle cx="26" cy="26" r="26" fill="#2bb3b6"/><path d="M26 13c-5.5 0-9.5 4-9.5 9.2 0 6.8 9.5 17 9.5 17s9.5-10.2 9.5-17C35.5 17 31.5 13 26 13z" fill="#fff"/><circle cx="26" cy="22.5" r="3.6" fill="#2bb3b6"/></svg>
      4175 N. Larchmont, Puyallup, WA 98461
    </div>
  </section>

  <section class="back">
    <div class="headshot" role="img" aria-label="Headshot portrait of Dr. Marcus Whitfield"></div>
    <div class="caption">Dr. Marcus Whitfield, MD PhD<br>Radiation Oncology</div>

    <div class="headline-band"><h2 class="headline">Exceeding Expectations One Patient at a Time</h2></div>

    <div class="about-box">
      <p>The leading cancer care treatment center in the South Puget Sound Region of Washington State.&nbsp; We customize a treatment plan for your unique diagnosis.</p>
      <p>Harbor Oncology Partners has been serving patients in the South Puget Sound Region with offices located in Puyallup, Washington. Our Cancer Treatment Center is made up of highly skilled medical professionals who deeply value your health and wellbeing. We take great pride in providing our community with high quality, patient-centric care and health education.</p>
      <p class="spaced">Proactive and preventative measures help keep our community healthier, and we work with that idea in mind. Harbor Oncology Partners has the wellness services you'd like when you're feeling fine, and the emergency services you need when illness or injury strikes. Come in for a check-up.</p>
    </div>
  </section>

</div>
</body>
</html>
```